FERNGATE BUILDERS Van Wrap Design

Ferngate builders is looking for a new vehicle wrap for our trade vans
Needs to have our LOGO, PHONE NUMBER (02278619405) QTC LOGO, CRAFT TRADES GUILD LOGO
Something big bold and attractive. The windows are tinted black but could be wrapped in white to continue the design
I have attached some ideas - we would like half wrap or full wrap

(I have attached our OLD van wrap with our OLD logo only for reference - do not copy as this is outdated)

```html
<!DOCTYPE html>
<html lang="en">
<head>
<meta charset="utf-8">
<title>Ferngate Builders – Van Wrap Design</title>
<link rel="stylesheet" href="https://fonts.googleapis.com/css2?family=Montserrat:wght@400;500;600;700&display=swap">
<style>
  :root {
    --navy: #0f2447;
    --silver: #d5d6d8;
    --silver-dark: #b9bbbe;
    --white: #ffffff;
    --glass: #1d1f22;
    --trim: #2a2b2e;
    --tyre: #141414;
    --rim: #c9cbce;
    --tail: #b3232b;
    --backdrop: #ececec;
  }
  html, body { margin: 0; padding: 0; overflow: hidden; }
  body { width: 1200px; height: 1000px; }
  .canvas {
    position: relative; width: 1200px; height: 1000px; overflow: hidden;
    background: radial-gradient(ellipse at 50% 45%, #f7f7f7 0%, var(--backdrop) 60%, #dcdcdc 100%);
    font-family: "Montserrat", Arial, sans-serif;
  }
  .artwork { position: absolute; left: 0; top: 0; }
  .text { position: absolute; margin: 0; white-space: nowrap; line-height: 1; }
  .brand-name { color: var(--white); font-weight: 600; letter-spacing: 0.14em; text-align: center; }
  .brand-tagline { color: var(--white); font-weight: 400; letter-spacing: 0.12em; text-align: center; }
  .services { color: var(--navy); font-weight: 500; font-size: 12.5px; line-height: 1.25; }
  .phone { color: var(--navy); font-weight: 700; font-size: 21px; letter-spacing: 0.02em; }
  .email { color: var(--navy); font-weight: 500; font-size: 11px; }
  .front-name { color: var(--tail); font-weight: 600; font-size: 10px; letter-spacing: 0.1em; }
  .rear .phone, .rear .email, .rear .brand-name, .rear .brand-tagline { color: var(--white); }
</style>
</head>
<body>
<main class="canvas">
  <svg class="artwork" width="1200" height="1000" viewBox="0 0 1200 1000" aria-hidden="true">
    <defs>
      <g id="van-side">
        <path class="body-silver" fill="var(--silver)" d="M70 232 L82 215 L540 215 Q600 222 660 268 L740 326 Q790 340 795 380 L798 440 L775 452 H70 Z"/>
        <path class="wrap-navy" fill="var(--navy)" d="M70 232 L82 215 L545 217 Q370 280 345 452 H70 Z"/>
        <path class="wrap-gap" fill="none" stroke="var(--white)" stroke-width="5" d="M551 218 Q377 281 351 452"/>
        <path class="wrap-edge" fill="none" stroke="var(--navy)" stroke-width="3" d="M559 220 Q385 283 359 452"/>
        <path class="cab-window" fill="var(--glass)" d="M470 242 L560 238 Q610 265 652 318 L470 318 Z"/>
        <rect class="mirror" x="582" y="282" width="22" height="26" rx="4" fill="var(--silver-dark)"/>
        <rect class="door-handle" x="470" y="322" width="30" height="6" rx="3" fill="var(--silver-dark)"/>
        <path class="bumper" fill="var(--trim)" d="M690 400 L798 392 L798 440 L775 452 L690 452 Z"/>
        <rect class="sill" x="70" y="438" width="720" height="14" fill="var(--trim)"/>
        <rect class="tail-light" x="74" y="296" width="20" height="88" rx="3" fill="var(--tail)"/>
        <path class="arch" fill="var(--trim)" d="M170 452 A55 55 0 0 1 280 452 Z M600 452 A55 55 0 0 1 710 452 Z"/>
        <circle cx="225" cy="445" r="40" fill="var(--tyre)"/><circle cx="225" cy="445" r="26" fill="var(--rim)"/>
        <circle cx="655" cy="445" r="40" fill="var(--tyre)"/><circle cx="655" cy="445" r="26" fill="var(--rim)"/>
        <!-- accreditation badges on the silver panel -->
        <circle class="badge-qtc" cx="420" cy="358" r="20" fill="var(--navy)"/>
        <rect class="badge-guild" x="408" y="394" width="24" height="34" fill="var(--navy)"/>
      </g>
    </defs>

    <use href="#van-side" class="van-side-right"/>
    <use href="#van-side" class="van-side-left" transform="translate(865 315) scale(-1 1)"/>

    <g class="van-front">
      <path d="M842 225 Q845 208 860 206 H1092 Q1107 208 1110 225 V470 H842 Z" fill="var(--white)"/>
      <rect x="842" y="206" width="268" height="10" fill="var(--navy)"/>
      <rect x="842" y="219" width="268" height="3" fill="var(--navy)"/>
      <path d="M862 240 H1090 L1098 318 H854 Z" fill="var(--glass)"/>
      <rect x="815" y="284" width="26" height="34" rx="5" fill="var(--silver-dark)"/>
      <rect x="1111" y="284" width="26" height="34" rx="5" fill="var(--silver-dark)"/>
      <path d="M848 340 H900 L905 368 H848 Z M1104 340 H1052 L1047 368 H1104 Z" fill="var(--silver-dark)"/>
      <rect x="842" y="370" width="268" height="100" rx="6" fill="var(--trim)"/>
      <rect x="885" y="380" width="182" height="16" fill="var(--glass)"/>
      <rect x="885" y="425" width="182" height="14" fill="var(--glass)"/>
      <rect x="846" y="470" width="36" height="14" fill="var(--tyre)"/>
      <rect x="1070" y="470" width="36" height="14" fill="var(--tyre)"/>
    </g>

    <g class="van-rear">
      <path d="M842 530 Q845 516 860 515 H1092 Q1107 516 1110 530 V740 H842 Z" fill="var(--navy)"/>
      <rect x="818" y="595" width="22" height="34" rx="4" fill="var(--trim)"/>
      <rect x="1112" y="595" width="22" height="34" rx="4" fill="var(--trim)"/>
      <rect x="844" y="612" width="24" height="88" rx="3" fill="var(--tail)"/>
      <rect x="1084" y="612" width="24" height="88" rx="3" fill="var(--tail)"/>
      <rect x="842" y="738" width="268" height="50" rx="4" fill="var(--trim)"/>
      <rect x="846" y="788" width="36" height="10" fill="var(--tyre)"/>
      <rect x="1070" y="788" width="36" height="10" fill="var(--tyre)"/>
    </g>
  </svg>

  <section class="side right">
    <p class="text brand-name" style="left:110px; top:282px; width:260px; font-size:30px;">FERNGATE</p>
    <p class="text brand-name" style="left:110px; top:326px; width:260px; font-size:28px;">BUILDERS</p>
    <p class="text brand-tagline" style="left:110px; top:362px; width:260px; font-size:13.5px;">LICENSED CARPENTERS</p>
    <p class="text services" style="left:462px; top:350px;">New Homes, Renovations<br>&amp; Commercial Buildings</p>
    <p class="text phone" style="left:462px; top:380px;">022·786·19405</p>
    <p class="text email" style="left:462px; top:404px;">info@ferngatebuilders.co.nz</p>
  </section>

  <section class="side left">
    <p class="text brand-name" style="left:495px; top:597px; width:260px; font-size:30px;">FERNGATE</p>
    <p class="text brand-name" style="left:495px; top:641px; width:260px; font-size:28px;">BUILDERS</p>
    <p class="text brand-tagline" style="left:495px; top:677px; width:260px; font-size:13.5px;">LICENSED CARPENTERS</p>
    <p class="text services" style="left:252px; top:661px;">New Homes, Renovations<br>&amp; Commercial Buildings</p>
    <p class="text phone" style="left:252px; top:691px;">022·786·19405</p>
    <p class="text email" style="left:252px; top:715px;">info@ferngatebuilders.co.nz</p>
  </section>

  <p class="text front-name" style="left:842px; top:322px; width:268px; text-align:center;">FERNGATE BUILDERS</p>

  <section class="rear">
    <p class="text brand-name" style="left:842px; top:556px; width:268px; font-size:17px;">FERNGATE</p>
    <p class="text brand-name" style="left:842px; top:578px; width:268px; font-size:15px;">BUILDERS</p>
    <p class="text brand-tagline" style="left:842px; top:596px; width:268px; font-size:8.5px;">LICENSED CARPENTERS</p>
    <p class="text phone" style="left:842px; top:608px; width:268px; text-align:center; font-size:17px;">022·786·19405</p>
    <p class="text email" style="left:842px; top:628px; width:268px; text-align:center; font-size:9.5px;">info@ferngatebuilders.co.nz</p>
  </section>
</main>
</body>
</html>
```